Congressional Website with splash page for Texas Democratic Black Woman

I would like a splash page with a turquoise shaded theme to it. My logo can be played with but the original logo is black white and red... we are now wanting a page that is in shades of turquoise with the black white and red colors. On the splash page, I want to collect volunteer information and prompt people to donate. I would like to.just have a large picture of me of some sort and then you have to click to enter the rest of the page with the issues.

Target Market(s)

Voters and Donors and democrats

Industry/Entity Type

campaign/elections

Coding

Coded - Design and coding required

Number of Pages Required

2 page

Font styles to use
Serif

Colors
0094D4
00A9DD
6FCCEA
C7EBF8
E9F6FB

Requirements
Must have
• I must have a landing page... and then it open up to the other pages.

```html
<!DOCTYPE html>
<html lang="en">
<head>
<meta charset="utf-8">
<title>About Renata Holloway</title>
<link rel="stylesheet" href="https://fonts.googleapis.com/css2?family=Oswald:wght@300;400;500&family=Lato:wght@400&display=swap">
<style>
:root{
  --blue:#0094d4;
  --blue-mid:#00a9dd;
  --blue-light:#6fccea;
  --ink:#2b2b2b;
  --text:#3a3a3a;
  --red:#f50018;
  --black:#000;
  --white:#fff;
  --footer:#222;
}
*{margin:0;padding:0;box-sizing:border-box}
html,body{width:885px;height:1200px;overflow:hidden;background:var(--white)}
body{position:relative;font-family:'Lato',sans-serif;color:var(--text)}
.hero{position:absolute;left:0;top:0;width:885px;height:336px;
  background:radial-gradient(ellipse at 48% 40%,#1a78b8 0%,var(--blue) 45%,#2aa3e3 100%)}
.brand{position:absolute;left:55px;top:22px;width:240px;color:var(--white)}
.brand-name{font-family:'Oswald',sans-serif;font-weight:400;font-size:40px;line-height:1;letter-spacing:1px;padding-bottom:8px;border-bottom:2px solid var(--white)}
.brand-tag{font-family:'Oswald',sans-serif;font-weight:500;font-size:15.5px;letter-spacing:1.6px;padding:6px 6px;border-bottom:2px solid var(--white)}
.btn{position:absolute;top:59px;height:38px;display:flex;align-items:center;justify-content:center;font-family:'Oswald',sans-serif;font-weight:400;font-size:14.5px;color:var(--white);letter-spacing:.3px}
.btn-volunteer{left:553px;width:167px;border:1.5px solid var(--white)}
.btn-donate{left:727px;width:104px;background:var(--black)}
.hero-title{position:absolute;left:0;width:885px;top:190px;text-align:center;font-family:'Oswald',sans-serif;font-weight:400;font-size:48px;color:var(--white);letter-spacing:.5px}
.section-title{position:absolute;left:55px;font-family:'Oswald',sans-serif;font-weight:400;font-size:30px;color:var(--ink)}
.about-title{top:388px}
.about-copy{position:absolute;left:55px;top:436px;width:384px;font-size:12.4px;line-height:23.2px}
.btn-read{position:absolute;left:55px;top:641px;width:132px;height:41px;background:var(--red);color:var(--white);font-family:'Oswald',sans-serif;font-size:15px;display:flex;align-items:center;justify-content:center}
.about-photo{position:absolute;left:454px;top:394px;width:377px;height:288px;
  background:linear-gradient(90deg,#5a3a26 0%,#a8835f 30%,#e8e2da 55%,#5b3523 100%)}
.more-title{top:731px}
.facts{position:absolute;top:789px;width:375px;list-style:none}
.facts-left{left:55px}
.facts-right{left:454px}
.facts li{position:relative;padding-left:25px;font-size:12.4px;line-height:19.5px;margin-bottom:10px}
.facts li svg{position:absolute;left:0;top:5px}
.footer{position:absolute;left:0;top:1113px;width:885px;height:87px;background:var(--footer)}
.copyright{position:absolute;left:54px;top:37px;font-size:10px;color:var(--white)}
.social{position:absolute;top:36px;display:flex;gap:20px;left:678px}
.social span{width:15px;height:15px;border-radius:50%;background:var(--white)}
</style>
</head>
<body>
<header class="hero" role="img" aria-label="Blue-tinted photo of the candidate seated on a wooden bench">
  <div class="brand">
    <div class="brand-name">RENATA HOLLOWAY</div>
    <div class="brand-tag">DEMOCRAT FOR US CONGRESS</div>
  </div>
  <a class="btn btn-volunteer">VOLUNTEER INFORMATION</a>
  <a class="btn btn-donate">DONATE</a>
  <h1 class="hero-title">ABOUT RENATA</h1>
</header>

<h2 class="section-title about-title">ABOUT RENATA</h2>
<p class="about-copy">Sed ut perspiciatis unde omnis iste natus error sit voluptatem accusantium doloremque laudantium, totam rem aperiam, eaque ipsa quae ab illo inventore veritatis et quasi architecto beatae vitae dicta sunt explicabo. Nemo enim ipsam voluptatem quia voluptas sit aspernatur aut odit aut fugit, sed quia consequuntur magni dolores eos qui ratione voluptatem sequi nesciunt. Neque porro quisquam est, qui dolorem ipsum quia dolor sit amet, consectetur, adipisci velit, sed quia non numquam.</p>
<a class="btn-read">READ MORE</a>
<div class="about-photo" role="img" aria-label="Portrait of the candidate in a white blazer seated at a wooden desk beside a brass lamp"></div>

<h2 class="section-title more-title">MORE ABOUT RENATA</h2>
<svg width="0" height="0" style="position:absolute">
  <symbol id="chev" viewBox="0 0 10 9"><path d="M1 1l3.5 3.5L1 8M5.5 1L9 4.5 5.5 8" fill="none" stroke="#0094d4" stroke-width="1.8"/></symbol>
</svg>
<ul class="facts facts-left">
  <li><svg width="10" height="9"><use href="#chev"/></svg>Civil Rights, Criminal Defense, &amp; Personal Injury Attorney</li>
  <li><svg width="10" height="9"><use href="#chev"/></svg>Zeta Omicron Rho</li>
  <li><svg width="10" height="9"><use href="#chev"/></svg>Youngest Black Member</li>
  <li><svg width="10" height="9"><use href="#chev"/></svg>Filed more bills than any other freshmen legislator</li>
  <li><svg width="10" height="9"><use href="#chev"/></svg>Named Freshman of the year by the State Legislative Black Caucus &amp; Metro Observer</li>
  <li><svg width="10" height="9"><use href="#chev"/></svg>Named most effective freshman by Lone Star Quarterly</li>
  <li><svg width="10" height="9"><use href="#chev"/></svg>Represented over 400+ peaceful protestors pro Bono</li>
  <li><svg width="10" height="9"><use href="#chev"/></svg>Only currently elected official in the race</li>
  <li><svg width="10" height="9"><use href="#chev"/></svg>Only female attorney in this race</li>
</ul>
<ul class="facts facts-right">
  <li><svg width="10" height="9"><use href="#chev"/></svg>One of the main leaders of the State Democratic<br>Quorum Break</li>
  <li><svg width="10" height="9"><use href="#chev"/></svg>Serves on the powerful Business &amp; Industry Committee &amp; Criminal Jurisprudence Committee</li>
  <li><svg width="10" height="9"><use href="#chev"/></svg>Daughter of a preacher and teacher, and parents are lifelong servants leaders</li>
  <li><svg width="10" height="9"><use href="#chev"/></svg>Harlow College</li>
  <li><svg width="10" height="9"><use href="#chev"/></svg>Marlow School of Law and Bayside University Law Center</li>
  <li><svg width="10" height="9"><use href="#chev"/></svg>Represented the families of Darnell Hayes, Marcus Price, Alicia Monroe, Denise Carter and many more victims of police brutality.</li>
</ul>

<footer class="footer">
  <p class="copyright">Copyright © 2021. Company Name All Right Reserved</p>
  <div class="social" aria-label="Social links"><span></span><span></span><span></span><span></span><span></span></div>
</footer>
</body>
</html>
```